AMAZING WEBSITE DESIGN NEEDED FOR MAID / CLEANING SERVICE

NOTE: This is Website Design Only - No coding required

Please submit your designs ASAP as we want to pick a winner and get started!

Hey,

We are looking for a new amazing website design for a maid or cleaning service.

They have a horrible website that we want turned into a masterpiece.

As you will see on their current site:

http://tidyharborco.examplehost.net/

They have a lot of stuff, very disorganized, and need help.

Here is what we need:

Colors: Same as current site, Orange, Gray, Black

Menu: Horizontal with same Menu items

Need a spot for a video on the homepage

Want content to be structured in a great format that is easy to read.

Want to highlight commercial and residential on the website homepage.

Also want a spot for customer testimonials

We want the site clean, professional, fresh and modern.

Please help by matching the logo design.

I look forward to your designs!
Updates

Hi All! Really appreciate your efforts and designs. I will be meeting with our client on Monday and will then be able to provide feedback after our meeting. If you have other ideas, please submit them. The more I can show him the better! Thanks!

Target Market(s)

The target market is residential home owners as well as commercial businesses who need cleaning on a regular basis.

This company cleans homes and offices for individuals.

Industry/Entity Type

Residential

Font styles to use
Sans Serif

Requirements
Must have
• Must match logo colors
Must have spot for video
Must have a clean look
Must have a bold look
Nice to have
• Highly visual
Should not have
• clutter
messy design
hard to read

```html
<!DOCTYPE html>
<html lang="en">
<head>
<meta charset="utf-8">
<title>Tidy Harbor – Quality Commercial &amp; Residential Cleaning</title>
<link href="https://fonts.googleapis.com/css2?family=Arvo&family=Lato:ital,wght@0,400;0,700;1,400&display=swap" rel="stylesheet">
<style>
  :root{
    --orange:#f26a1b;
    --orange-light:#fb8a3c;
    --gray-dark:#4d4d4d;
    --gray-mid:#8a8a8a;
    --gray-line:#d4d4d4;
    --card-bg:#f3f3f3;
    --text:#333333;
    --white:#ffffff;
  }
  *{box-sizing:border-box;margin:0;padding:0}
  html,body{width:763px;height:1200px;overflow:hidden;background:var(--white)}
  body{font-family:"Lato",Arial,sans-serif;color:var(--text)}
  .page{position:relative;width:763px;height:1200px;overflow:hidden}

  /* header */
  .brand{position:absolute;left:22px;top:46px}
  .brand-name{display:flex;align-items:center;gap:7px;font-family:"Lato",sans-serif;font-weight:700;font-size:25px;color:var(--orange);line-height:1}
  .brand-mark{width:16px;height:16px;background:var(--orange)}
  .brand-tagline{font-size:9.5px;font-style:italic;color:var(--gray-dark);margin-top:6px;font-weight:700}
  .contact-line{position:absolute;right:14px;top:10px;font-size:12.5px;color:var(--gray-dark);text-decoration:underline}
  .search{position:absolute;left:530px;top:41px;display:flex;gap:6px}
  .search-field{width:178px;height:22px;border:1px solid #bdbdbd;background:var(--white)}
  .search-go{width:38px;height:22px;border:1px solid #bdbdbd;background:linear-gradient(#fafafa,#dcdcdc);font:700 12px "Lato",sans-serif;color:var(--text)}

  .main-nav{position:absolute;left:220px;top:77px;width:543px;height:30px;background:var(--gray-dark);display:flex;align-items:center;padding-left:36px}
  .main-nav a,.footer-nav a{color:var(--white);text-decoration:none;font-size:11.5px}
  .main-nav .sep,.footer-nav .sep{color:#cfcfcf;font-size:11px;margin:0 11px}

  /* slider */
  .slider{position:absolute;left:0;top:111px;width:763px;height:239px;background:var(--white)}
  .slide{position:absolute;top:0;height:239px}
  .slide-left{left:0;width:276px;background:linear-gradient(160deg,#f3f5f8 0%,#dbe4ee 55%,#3d74b4 100%)}
  .slide-center{left:280px;width:240px;background:radial-gradient(ellipse at 50% 60%,#3e8fd6 0%,#f3e06b 45%,#ffffff 80%)}
  .slide-right{left:590px;width:173px;background:linear-gradient(180deg,#ffffff 0%,#a7795a 40%,#2b5fa6 100%)}
  .slider-arrow{position:absolute;top:86px}
  .slider-dots{position:absolute;left:328px;top:221px;display:flex;gap:9px}
  .slider-dots span{width:10px;height:10px;border-radius:50%;border:1.5px solid var(--orange);background:var(--white)}
  .slider-dots span.active{background:var(--orange)}
  .slider-rule{position:absolute;left:0;top:350px;width:763px;height:5px;background:#5e5e5e}

  /* info cards */
  .info-card{position:absolute;top:383px;width:223px;height:140px;border:1px solid var(--gray-line);border-radius:6px;background:linear-gradient(#ffffff,#ececec);padding:8px 14px}
  .info-card h3{font-family:"Arvo",serif;font-weight:400;font-size:16px;line-height:19px;color:var(--orange)}
  .info-card p{font-size:11.5px;line-height:15px;color:var(--text);margin-top:2px}
  .btn-more{position:absolute;left:18px;bottom:-8px;width:96px;height:28px;border-radius:5px;background:linear-gradient(var(--orange-light),var(--orange));color:var(--white);font-size:11.5px;display:flex;align-items:center;justify-content:center;box-shadow:0 1px 2px rgba(0,0,0,.3)}

  /* welcome */
  .welcome{position:absolute;left:20px;top:559px;width:425px}
  .welcome h1{font-family:"Arvo",serif;font-weight:400;font-size:23px;color:var(--orange);line-height:26px}
  .welcome p{font-size:12.3px;line-height:13.9px;color:var(--text);margin-top:1px}
  .video-title{position:absolute;left:468px;top:570px;font-size:14.5px;color:var(--text)}
  .video-frame{position:absolute;left:460px;top:592px;width:277px;height:166px;border-radius:6px;background:linear-gradient(135deg,#eef2f5 0%,#cfd8de 40%,#7f8f9c 70%,#3d6c92 100%);overflow:hidden}
  .video-play{position:absolute;left:113px;top:58px}

  /* features */
  .feature{position:absolute;top:823px;width:223px;height:191px;border:1px solid var(--gray-line);border-radius:6px;background:linear-gradient(#ffffff,#ececec);font-family:"Arvo",serif}
  .feature-art{position:absolute}
  .feature-lead{position:absolute;color:var(--orange);font-size:13px;line-height:15px}
  .feature-body{position:absolute;left:14px;color:var(--text);font-size:12.5px;line-height:15px}

  .local-line{position:absolute;left:20px;top:1038px;font-family:"Arvo",serif;font-size:14px;color:var(--text)}
  .impressions{position:absolute;left:20px;top:1064px;width:720px;font-family:"Arvo",serif;font-size:14px;line-height:18px;color:var(--text)}
  .to-top{position:absolute;left:714px;top:1117px}

  /* footer */
  .site-footer{position:absolute;left:0;top:1150px;width:763px;height:50px;background:var(--gray-dark)}
  .footer-nav{position:absolute;left:0;top:12px;width:763px;display:flex;justify-content:center;padding-right:30px}
  .footer-nav a{font-size:10px}
  .copyright{position:absolute;left:0;top:34px;width:763px;text-align:center;color:var(--white);font-size:9px}
</style>
</head>
<body>
<div class="page">

  <header>
    <div class="brand">
      <div class="brand-name"><span class="brand-mark"></span>Tidy Harbor</div>
      <div class="brand-tagline">Quality Commercial &amp; Residential Cleaning</div>
    </div>
    <div class="contact-line">Tidy Harbor, LLC | Albuquerque, New Mexico | (505) 555-0182 office</div>
    <form class="search">
      <div class="search-field"></div>
      <button class="search-go" type="button">Go!</button>
    </form>
    <nav class="main-nav">
      <a href="#">Home</a><span class="sep">|</span>
      <a href="#">About Us</a><span class="sep">|</span>
      <a href="#">Our Services</a><span class="sep">|</span>
      <a href="#">Our Employees</a><span class="sep">|</span>
      <a href="#">Special Offers</a><span class="sep">|</span>
      <a href="#">Contact Us</a>
    </nav>
  </header>

  <section class="slider">
    <div class="slide slide-left" role="img" aria-label="Photo of a smiling cleaner in an apron scrubbing the floor beside a blue bucket"></div>
    <div class="slide slide-center" role="img" aria-label="Photo of a blue bucket filled with cleaning supplies, gloves and a feather duster"></div>
    <div class="slide slide-right" role="img" aria-label="Photo of a smiling housekeeper in a blue apron holding yellow gloves"></div>
    <svg class="slider-arrow" style="left:14px" width="32" height="32" viewBox="0 0 32 32"><circle cx="16" cy="16" r="14" fill="#fff" stroke="#9a9a9a" stroke-width="2"/><path d="M19 9 L12 16 L19 23" fill="none" stroke="#8a8a8a" stroke-width="3"/></svg>
    <svg class="slider-arrow" style="left:716px" width="32" height="32" viewBox="0 0 32 32"><circle cx="16" cy="16" r="14" fill="#fff" stroke="#9a9a9a" stroke-width="2"/><path d="M13 9 L20 16 L13 23" fill="none" stroke="#8a8a8a" stroke-width="3"/></svg>
    <div class="slider-dots"><span class="active"></span><span></span><span></span><span></span><span></span></div>
  </section>
  <div class="slider-rule"></div>

  <article class="info-card" style="left:21px">
    <h3>What Our Customers<br>Are Saying</h3>
    <p>Lorem Ipsum is simply dummy text<br>of the printing and typesetting industry<br>Lorem Ipsum has been the industry</p>
    <div class="btn-more">READ MORE</div>
  </article>
  <article class="info-card" style="left:271px">
    <h3>Why Choose Tidy<br>Harbor?</h3>
    <p>Lorem Ipsum is simply dummy text<br>of the printing and typesetting industry<br>Lorem Ipsum has been the industry</p>
    <div class="btn-more">READ MORE</div>
  </article>
  <article class="info-card" style="left:519px">
    <h3>Meet the President &amp;<br>CEO</h3>
    <p>Lorem Ipsum is simply dummy text<br>of the printing and typesetting industry<br>Lorem Ipsum has been the industry</p>
    <div class="btn-more">READ MORE</div>
  </article>

  <section class="welcome">
    <h1>Welcome to our website!</h1>
    <p>Thank you for visiting us! You are one step closer to experiencing first class maid service! Our company specializes in detailed housekeeping, janitorial, and commerical cleaning services making your environment shine and sparkle like it never has before! Our maids are fully trained professionals who we recruit from high end luxury hotels we know, like the Grand Lumen and Bayview Suites! We pride ourselves in delivering exceptional service to our valued customers by fully understanding what your expectations &amp; needs are! We will strive for perfection and we will provide an uncompromising commitment to excellence! Our "unlimited" name gives us an edge over our competition by giving you access to more home and office cleaning services for absolutely no extra costs! Why pay more for less?? NEVER have any hidden charges, overages, or sneaky fees! With Tidy Harbor start getting more for your dollar! Your wish is our command and that is the true "Tidy Harbor" way! Call us today!</p>
  </section>

  <div class="video-title">Lorem Ipsum is play this video</div>
  <div class="video-frame" role="img" aria-label="Video still of cleaners tidying a bright living room">
    <svg class="video-play" width="50" height="50" viewBox="0 0 50 50"><circle cx="25" cy="25" r="22" fill="rgba(255,255,255,.35)" stroke="#fff" stroke-width="3"/><path d="M20 15 L35 25 L20 35 Z" fill="#fff"/></svg>
  </div>

  <article class="feature" style="left:21px">
    <div class="feature-art" role="img" aria-label="Eco friendly green globe badge" style="left:14px;top:12px;width:86px;height:86px;border-radius:50%;background:radial-gradient(circle at 40% 35%,#9bd44a,#3e8f1f)"></div>
    <div class="feature-lead" style="left:134px;top:60px">Tidy<br>Harbor is<br>commited<br>to using</div>
    <div class="feature-body" style="top:122px">Eco Green chemicals to keep<br>you and your family safe! No<br>harsh chemicals here!</div>
  </article>
  <article class="feature" style="left:270px">
    <div class="feature-art" role="img" aria-label="Pink awareness ribbon" style="left:36px;top:10px;width:38px;height:112px;border-radius:19px 19px 4px 4px;background:linear-gradient(#f9a7c8,#e95592)"></div>
    <div class="feature-lead" style="left:106px;top:70px">Tidy Harbor<br>proudly donates<br>1% of its<br>earnings to</div>
    <div class="feature-body" style="top:138px">find a cure for breast cancer!<br>Be part of a life changing<br>cause!</div>
  </article>
  <article class="feature" style="left:519px">
    <div class="feature-art" role="img" aria-label="Gold satisfaction guarantee seal" style="left:14px;top:12px;width:96px;height:96px;border-radius:50%;background:radial-gradient(circle,#f7d76a,#b8860b)"></div>
    <div class="feature-lead" style="left:124px;top:40px;font-size:14px;line-height:16px;text-align:right;width:90px">Satisfaction<br>Guaranteed!</div>
    <div class="feature-body" style="top:117px">We guarantee you will be<br>100% satisfied with our<br>cleaning and our cleaning<br>professionals!</div>
  </article>

  <p class="local-line">Locally Owned &amp; Operated Never deal with an unresponsive franchise - Deal with the owner!</p>
  <p class="impressions">First Impressions are everything!! They will make you or break you. Blow your clients away with a sparkling clean office building, a professional maid staff,&nbsp; and an enjoyable comfortable waiting area for your clients to wait!</p>
  <svg class="to-top" width="28" height="28" viewBox="0 0 28 28" aria-label="Back to top"><circle cx="14" cy="14" r="12.5" fill="#fff" stroke="#9a9a9a" stroke-width="1.5"/><path d="M8 17 L14 10 L20 17 Z" fill="#9a9a9a"/></svg>

  <footer class="site-footer">
    <nav class="footer-nav">
      <a href="#">Home</a><span class="sep">|</span>
      <a href="#">About Us</a><span class="sep">|</span>
      <a href="#">Our Services</a><span class="sep">|</span>
      <a href="#">Our Employees</a><span class="sep">|</span>
      <a href="#">Special Offers</a><span class="sep">|</span>
      <a href="#">Contact Us</a>
    </nav>
    <div class="copyright">Copyright © Tidy Harbor. All rights reserved.</div>
  </footer>

</div>
</body>
</html>
```